Business card design needed

Family General Practitioner/ Family Physician.
Logo is the logo of the Imperial Guild of Community Clinicians Oceania
http://pkvtm.lorimar.example/PictureGallery/logos/pages/IGCCO%20logo_jpg.htm

Reason: Just a bit more time to make changes and the weekend for me to look at things closely and to choose. Thanks, Ulan

Thanks for all the submissions. So many of them are really works of art. Not one of them are not good. The ones that I am eliminating are the ones that I think are not suitable for me personally only, and because if I don't, it makes it very difficult to decide as many of you are also sending me slight variations of a card. I have just decided to choose a second place card too. Can't thank you all enough. Good luck, Ulan. P.S - Working today till 10 pm as the card says :-), so probably won't be able to give a feedback till late Saturday night or Sunday morning here in Sydney, Australia. 

Reason: Just added a second place to the budget and realised that Australia is ahead of the rest of the world in the time zone (only :-) - don't want to offend anyone or start a debate!! ) , so Monday deadline will mean it will be a weekend for the rest of the world. Just wanted to give everyone more time to submit their best, especially since I will be picking a second card too. Can't thank everyone enough for the submissions. P.S - Not keen on photos on the card.

Business

Contact Information for Business Card

Dr. Ulan Pereira M.B.B.S., F.I.G.C.C.O
Family General Practitioner
Address, timings, phone and fax number on the back.

Requirements
Must have
• Timings
Mon 7 am - 7 pm
Tues 7 am - 12 pm
Wed 7 am - 10 pm
Thurs 7 am - 12 pm
Fri 7 am - 8 pm
Sat 8 am - 10 pm
Sun - Off

```html
<!DOCTYPE html>
<html lang="en">
<head>
<meta charset="utf-8">
<title>Dr. Ulan Pereira – Business Card</title>
<link href="https://fonts.googleapis.com/css2?family=Jost:wght@400;500&family=Source+Sans+3:wght@400;500&display=swap" rel="stylesheet">
<style>
  :root {
    --navy: #0f1236;
    --navy-deep: #0d1024;
    --pale: #eff3fd;
    --ink: #0f1650;
    --red: #c40f14;
    --rule: #1a1a1a;
    --white: #ffffff;
    --page: #fdfdfd;
  }
  html, body {
    margin: 0;
    width: 1200px;
    height: 1200px;
    overflow: hidden;
    background: var(--page);
  }
  .card {
    position: absolute;
    left: 68px;
    top: 275px;
    width: 1054px;
    height: 640px;
    overflow: hidden;
    font-family: "Source Sans 3", sans-serif;
  }
  .band-top {
    position: absolute; left: 0; top: 0; width: 100%; height: 209px;
    background: var(--navy);
  }
  .band-info {
    position: absolute; left: 0; top: 209px; width: 100%; height: 222px;
    background: var(--pale);
  }
  .band-bottom {
    position: absolute; left: 0; top: 431px; width: 100%; height: 209px;
    background: linear-gradient(var(--navy-deep), #0e1122);
  }
  .brand {
    position: absolute; right: 28px; top: 78px;
    display: flex; align-items: center; gap: 12px;
    color: var(--white);
    font-family: "Jost", sans-serif;
    font-weight: 500;
    font-size: 30px;
    letter-spacing: 3px;
  }
  .brand-dot {
    width: 22px; height: 22px; border-radius: 50%;
    background: var(--red);
  }
  .divider {
    position: absolute; top: 22px; width: 2px; height: 178px;
    background: var(--rule);
  }
  .divider.left { left: 63px; }
  .divider.mid { left: 599px; }
  .identity {
    position: absolute; left: 92px; top: 22px; width: 500px;
    text-align: center;
    font-family: "Jost", sans-serif;
  }
  .name {
    margin: 20px 0 0;
    font-size: 58px; font-weight: 500; color: var(--ink);
    letter-spacing: 2px; line-height: 1.1;
  }
  .credentials {
    margin: 4px 0 0;
    font-size: 21px; color: var(--ink); letter-spacing: 2px;
  }
  .role {
    margin: 6px 0 0;
    font-size: 28px; color: var(--red); letter-spacing: 2px;
  }
  .contact {
    position: absolute; left: 614px; top: 61px;
    font-size: 20px; line-height: 25px; color: #111;
    letter-spacing: -0.2px;
  }
  .contact p { margin: 0; }
  .hours-title {
    position: absolute; left: 0; top: 528px; width: 100%;
    text-align: center;
    font-family: "Jost", sans-serif;
    font-size: 24px; color: var(--white); letter-spacing: 10px;
  }
  .hours-rule {
    position: absolute; left: 12px; top: 567px; width: 1030px; height: 2px;
    background: #c9ccd6;
  }
  .hours {
    position: absolute; left: 18px; top: 588px; width: 1020px;
    display: flex; justify-content: space-between; align-items: center;
    margin: 0; padding: 0; list-style: none;
    font-size: 18.5px; color: var(--white);
  }
  .hours li { display: flex; align-items: center; white-space: nowrap; }
  .hours li + li::before {
    content: ""; display: inline-block; width: 3px; height: 28px;
    background: var(--white); margin-right: 9px;
  }
  .hours .closed { color: var(--red); }
</style>
</head>
<body>
  <div class="card">
    <div class="band-top">
      <div class="brand"><span class="brand-dot"></span>IGCCO</div>
    </div>
    <div class="band-info">
      <div class="divider left"></div>
      <div class="identity">
        <h1 class="name">Dr. Ulan Pereira</h1>
        <p class="credentials">M.B.B.S., F.I.G.C.C.O</p>
        <p class="role">FAMILY GENERAL PRACTITIONER</p>
      </div>
      <div class="divider mid"></div>
      <div class="contact">
        <p>IGCCO House, 48 Harlow Terrace,</p>
        <p>Eastmere, Victoria 3902 Australia</p>
        <p>Tel: +61 (3) 5550 0414 Fax: +61 (3) 5550 0400</p>
        <p>ABN 71 555 018 264</p>
      </div>
    </div>
    <div class="band-bottom"></div>
    <div class="hours-title">TIMINGS</div>
    <div class="hours-rule"></div>
    <ul class="hours">
      <li>Mon 7 am - 7 pm</li>
      <li>Tues 7 am - 12 pm</li>
      <li>Wed 7 am - 10 pm</li>
      <li>Thurs 7 am - 12 pm</li>
      <li>Fri 7 am - 8 pm</li>
      <li>Sat 8 am - 10 pm</li>
      <li><span class="closed">Sun - Off</span></li>
    </ul>
  </div>
</body>
</html>
```